Locksmith Store 475475 Signage

Design Brief: Locksmith Store Signage – "Locksmith 475475" [ΚΛΕΙΔΑΡΑΣ 475475 (in Greek)]
We are looking for a spectacular and professional sign design for the exterior of our locksmith store.
Signage Dimensions:
• Width: 6 meters
• Height: 1.5 meters
• Shopfront window Width: 6 meters, Height: 2.5 meters
Key Requirements (in order of importance):
1. It must be immediately clear that this is a locksmith store. [ΚΛΕΙΔΑΡΑΣ (in Greek)]
2. The store name "475475", (which is also the phone number 2310475475), should be highly visible and visually striking because this is the number that customers are calling when they are locked out.
3. The signage should also clearly communicate that except for house keys, which is obvious for a locksmith store the services we provide are:
o All kinds of house keys. ΚΛΕΙΔΙΑ ΣΠΙΤΙΩΝ(in Greek) (There is no key that we cannot do)
o Immobiliser car keys = ΚΛΕΙΔΙΑ ΑΥΤΟΚΙΝΗΤΩΝ (in Greek)
We unlock every car that exist, we program new immobilizer keys – remote controls, even if all keys are lost, we repair or change broken cells of car keys, we change batteries.
o High-security locks = ΚΛΕΙΔΑΡΙΕΣ ΑΣΦΑΛΕΙΑΣ (in Greek) we sell the best high security locks in the planet
o Armoured doors = ΠΟΡΤΕΣ ΑΣΦΑΛΕΙΑΣ (in Greek) (this may not be so important to be on the signage.
Visual Style:
We are open to creative direction, but the design should be eye-catching, professional, and modern, something that will stand out on a busy street and instantly tell customers who we are and what we offer. Also, you may use the shopfront window for graphic designs. Also, we are open if a part of the signage is digital.
________________________________________
Hello Designers,
Thank you so much for your effort and the designs you've shared.
I realized I forgot to mention that you can refer to my website at www.475475-keys.gr for more context.
Additionally, I’ve just uploaded two new photos: one showing the store with a black outline at the dimensions of the signage, and another with the large double-bit key placed in a different position to demonstrate that it is moveable.
Thanks again for your dedication!
every person that has a key

```html
<!DOCTYPE html>
<html lang="el">
<head>
<meta charset="utf-8">
<title>ΚΛΕΙΔΑΡΑΣ 475475 – Signage</title>
<link href="https://fonts.googleapis.com/css2?family=Archivo+Black&family=Roboto+Condensed:wght@700&family=Roboto:wght@700;900&display=swap" rel="stylesheet">
<style>
:root{
  --page:#b3b3b3;
  --label:#333333;
  --ink:#000000;
  --panel-hi:#2a2a2a;
  --red:#ff1a1a;
  --white:#ffffff;
  --gold-hi:#fbf3a6;
  --gold:#c9a83c;
  --gold-lo:#7d5f18;
  --gold-line:#e9df8a;
  --silver-hi:#ffffff;
  --silver-lo:#8c8c8c;
  --dark-text:#1a1a1a;
}
*{margin:0;padding:0;box-sizing:border-box}
html,body{width:1200px;height:923px;overflow:hidden}
body{background:var(--page);position:relative;font-family:"Roboto",Arial,sans-serif}
.size-label{position:absolute;left:0;width:1220px;text-align:center;font:700 27px/1 "Roboto",Arial,sans-serif;color:var(--label)}
.sign{position:absolute;left:125px;width:933px;overflow:hidden;
  background:radial-gradient(ellipse at 70% 35%,var(--panel-hi) 0%,#0c0c0c 55%,var(--ink) 100%)}
.sign--short{top:125px;height:233px}
.sign--tall{top:442px;height:388px}
.abs{position:absolute}
.key-art{background:radial-gradient(ellipse at 22% 50%,#fff6d0 0%,#d1a83e 22%,#6b5214 45%,rgba(0,0,0,0) 72%)}
.thumb{border:1.5px solid var(--white);border-radius:8px;background:#060606;display:flex;align-items:center;justify-content:center}
.thumb--gold{border-color:var(--gold-line)}
.thumb-art{width:55%;height:78%;border-radius:6px;background:linear-gradient(180deg,#d9d9d9,#6f6f6f 60%,#2b2b2b)}
.trade{font:700 48px/1 "Roboto Condensed","Arial Narrow",sans-serif;color:var(--red);white-space:nowrap;letter-spacing:-1px}
.number{font:400 72px/1 "Archivo Black","Arial Black",sans-serif;white-space:nowrap;letter-spacing:-2px;
  background:linear-gradient(180deg,var(--gold-hi) 0%,var(--gold) 55%,var(--gold-lo) 100%);
  -webkit-background-clip:text;background-clip:text;color:transparent}
.services{list-style:none}
.service{position:absolute;color:var(--white);font-weight:700;white-space:nowrap;display:flex;align-items:flex-start;gap:4px}
.service svg{flex:none}
.divider{border-left:1.5px dashed var(--white)}
.brand-mark{color:var(--white);font-family:"Roboto Condensed","Arial Narrow",sans-serif;font-weight:700;line-height:1.05;white-space:nowrap;display:flex;flex-direction:column;align-items:flex-start}
.phone-pill{border-radius:999px;background:linear-gradient(90deg,var(--silver-lo) 0%,var(--silver-hi) 40%,#e6e6e6 80%,#9a9a9a 100%);
  display:flex;align-items:center;color:var(--dark-text);font-weight:900;white-space:nowrap}
.phone-icon{border-radius:50%;background:#111;display:flex;align-items:center;justify-content:center;flex:none}
</style>
</head>
<body>

<div class="size-label" style="top:81px">6X1.5m</div>
<section class="sign sign--short">
  <div class="abs key-art" role="img" aria-label="Golden key entering a glowing keyhole" style="left:13px;top:46px;width:252px;height:147px"></div>
  <div class="abs trade" style="left:316px;top:28px">ΚΛΕΙΔΑΡΑΣ</div>
  <div class="abs number" style="left:287px;top:68px">475475</div>
  <ul class="services">
    <li class="service" style="left:280px;top:149px;font-size:11px"><svg width="8" height="8" viewBox="0 0 10 10"><circle cx="5" cy="5" r="5" fill="#ff1a1a"/><path d="M2.8 5.2l1.5 1.5 3-3" stroke="#fff" stroke-width="1.4" fill="none"/></svg>ΚΛΕΙΔΙΑ ΣΠΙΤΙΩΝ</li>
    <li class="service" style="left:433px;top:149px;font-size:11px"><svg width="8" height="8" viewBox="0 0 10 10"><circle cx="5" cy="5" r="5" fill="#ff1a1a"/><path d="M2.8 5.2l1.5 1.5 3-3" stroke="#fff" stroke-width="1.4" fill="none"/></svg>ΚΛΕΙΔΑΡΙΕΣ ΑΣΦΑΛΕΙΑΣ</li>
    <li class="service" style="left:280px;top:176px;font-size:11px"><svg width="8" height="8" viewBox="0 0 10 10"><circle cx="5" cy="5" r="5" fill="#ff1a1a"/><path d="M2.8 5.2l1.5 1.5 3-3" stroke="#fff" stroke-width="1.4" fill="none"/></svg>ΚΛΕΙΔΙΑ ΑΥΤΟΚΙΝΗΤΩΝ</li>
    <li class="service" style="left:433px;top:176px;font-size:11px"><svg width="8" height="8" viewBox="0 0 10 10"><circle cx="5" cy="5" r="5" fill="#ff1a1a"/><path d="M2.8 5.2l1.5 1.5 3-3" stroke="#fff" stroke-width="1.4" fill="none"/></svg>ΠΟΡΤΕΣ ΑΣΦΑΛΕΙΑΣ</li>
  </ul>
  <div class="abs divider" style="left:599px;top:32px;height:158px"></div>
  <div class="abs thumb" style="left:626px;top:31px;width:60px;height:102px"><div class="thumb-art" role="img" aria-label="House keys on a ring"></div></div>
  <div class="abs thumb thumb--gold" style="left:697px;top:31px;width:60px;height:102px"><div class="thumb-art" role="img" aria-label="Remote car key"></div></div>
  <div class="abs thumb" style="left:769px;top:31px;width:60px;height:102px"><div class="thumb-art" role="img" aria-label="Cylinder key"></div></div>
  <div class="abs thumb thumb--gold" style="left:840px;top:31px;width:60px;height:102px"><div class="thumb-art" role="img" aria-label="High-security key"></div></div>
  <div class="abs brand-mark" style="left:620px;top:155px;font-size:15px"><span>ΚΛΕΙΔΑΡΑΣ</span><span>2310 475.475</span></div>
  <div class="abs phone-pill" style="left:730px;top:155px;width:172px;height:32px;font-size:21px;gap:8px;padding-left:4px">
    <span class="phone-icon" style="width:24px;height:24px"><svg width="13" height="13" viewBox="0 0 24 24"><path fill="#fff" d="M6.6 10.8a15 15 0 006.6 6.6l2.2-2.2c.3-.3.7-.4 1-.2 1.1.4 2.3.6 3.6.6.6 0 1 .4 1 1V20c0 .6-.4 1-1 1A17 17 0 013 4c0-.6.4-1 1-1h3.5c.6 0 1 .4 1 1 0 1.3.2 2.5.6 3.6.1.3 0 .7-.2 1z"/></svg></span>2310475475</div>
</section>

<div class="size-label" style="top:397px">6X2.5m</div>
<section class="sign sign--tall">
  <div class="abs key-art" role="img" aria-label="Golden key entering a glowing keyhole" style="left:49px;top:23px;width:333px;height:198px"></div>
  <div class="abs thumb" style="left:50px;top:232px;width:71px;height:118px"><div class="thumb-art" role="img" aria-label="House keys on a ring"></div></div>
  <div class="abs thumb thumb--gold" style="left:134px;top:232px;width:71px;height:118px"><div class="thumb-art" role="img" aria-label="Remote car key"></div></div>
  <div class="abs thumb" style="left:218px;top:232px;width:71px;height:118px"><div class="thumb-art" role="img" aria-label="Cylinder key"></div></div>
  <div class="abs thumb thumb--gold" style="left:302px;top:232px;width:71px;height:118px"><div class="thumb-art" role="img" aria-label="High-security key"></div></div>
  <div class="abs trade" style="left:467px;top:28px;font-size:84px;letter-spacing:-2px">ΚΛΕΙΔΑΡΑΣ</div>
  <div class="abs number" style="left:422px;top:93px;font-size:120px;letter-spacing:-3px">475475</div>
  <ul class="services">
    <li class="service" style="left:427px;top:229px;font-size:15px;line-height:19px"><svg width="10" height="10" viewBox="0 0 10 10" style="margin-top:4px"><circle cx="5" cy="5" r="5" fill="#ff1a1a"/><path d="M2.8 5.2l1.5 1.5 3-3" stroke="#fff" stroke-width="1.4" fill="none"/></svg><span>ΚΛΕΙΔΙΑ<br>ΣΠΙΤΙΩΝ</span></li>
    <li class="service" style="left:521px;top:229px;font-size:15px;line-height:19px"><svg width="10" height="10" viewBox="0 0 10 10" style="margin-top:4px"><circle cx="5" cy="5" r="5" fill="#ff1a1a"/><path d="M2.8 5.2l1.5 1.5 3-3" stroke="#fff" stroke-width="1.4" fill="none"/></svg><span>ΚΛΕΙΔΙΑ<br>ΑΥΤΟΚΙΝΗΤΩΝ</span></li>
    <li class="service" style="left:662px;top:229px;font-size:15px;line-height:19px"><svg width="10" height="10" viewBox="0 0 10 10" style="margin-top:4px"><circle cx="5" cy="5" r="5" fill="#ff1a1a"/><path d="M2.8 5.2l1.5 1.5 3-3" stroke="#fff" stroke-width="1.4" fill="none"/></svg><span>ΚΛΕΙΔΑΡΙΕΣ<br>ΑΣΦΑΛΕΙΑΣ</span></li>
    <li class="service" style="left:791px;top:229px;font-size:15px;line-height:19px"><svg width="10" height="10" viewBox="0 0 10 10" style="margin-top:4px"><circle cx="5" cy="5" r="5" fill="#ff1a1a"/><path d="M2.8 5.2l1.5 1.5 3-3" stroke="#fff" stroke-width="1.4" fill="none"/></svg><span>ΠΟΡΤΕΣ<br>ΑΣΦΑΛΕΙΑΣ</span></li>
  </ul>
  <div class="abs brand-mark" style="left:428px;top:293px;font-size:25px"><span>ΚΛΕΙΔΑΡΑΣ</span><span>2310 475.475</span></div>
  <div class="abs phone-pill" style="left:611px;top:292px;width:290px;height:55px;font-size:36px;gap:14px;padding-left:7px">
    <span class="phone-icon" style="width:40px;height:40px"><svg width="21" height="21" viewBox="0 0 24 24"><path fill="#fff" d="M6.6 10.8a15 15 0 006.6 6.6l2.2-2.2c.3-.3.7-.4 1-.2 1.1.4 2.3.6 3.6.6.6 0 1 .4 1 1V20c0 .6-.4 1-1 1A17 17 0 013 4c0-.6.4-1 1-1h3.5c.6 0 1 .4 1 1 0 1.3.2 2.5.6 3.6.1.3 0 .7-.2 1z"/></svg></span>2310475475</div>
</section>

</body>
</html>
```